Business Card Design Project

Marla's Elixirs is a natural skincare business and we need a business card designed. The company focuses on natural products and will be launching with body scrubs and bath fizzies and our mission statement is: To deliver high quality natural beauty products at a good value. It's two cards - one design - the only information changing would be name and email address

Target Market(s)

Females ages 20-50

Industry/Entity Type

Business

Requirements
Must have
• Marla's Elixirs

Yvonne Hart-Becker
T: 800-555-7341
E: Yvonne@MarlasElixirs-example.com
W: www.MarlasElixirs-example.com

Tobias Werner
T: 800-555-7341
E: Tobias@MarlasElixirs-example.com
W: www.MarlasElixirs-example.com
Nice to have
• I'd like to use the colors or text found at www.marlaselixirs-example.com but I'm open to suggestions since design isn't set in stone yet. I would also like to have the words .....a little bit of magic somewhere under the company name in a different type of font. I would like a design that feels clean and maybe a retro feel to it - front and back would be nice but not mandatory

```html
<!DOCTYPE html>
<html lang="en">
<head>
<meta charset="utf-8">
<title>Marla's Elixirs – Business Cards</title>
<link rel="stylesheet" href="https://fonts.googleapis.com/css2?family=Open+Sans:wght@400;600&display=swap">
<style>
  :root {
    --page-bg: #e4e4e4;
    --magenta: #b0237f;
    --magenta-bright: #d1208f;
    --sky: #2fb0ea;
    --sky-deep: #1a7fd0;
    --sky-pale: #8fd8f6;
    --glow-pink: #f3b6e2;
    --white: #ffffff;
  }
  * { box-sizing: border-box; margin: 0; padding: 0; }
  html, body { width: 1200px; height: 900px; overflow: hidden; }
  body {
    background: var(--page-bg);
    display: flex;
    flex-direction: column;
    align-items: center;
    justify-content: center;
    gap: 40px;
    font-family: "Open Sans", sans-serif;
  }
  .card {
    position: relative;
    width: 700px;
    height: 400px;
    border-radius: 22px;
    overflow: hidden;
    background: linear-gradient(160deg, var(--sky-pale) 0%, var(--sky) 40%, var(--sky-deep) 100%);
    box-shadow: 0 6px 18px rgba(0,0,0,.18);
  }
  .card-art {
    position: absolute;
    inset: 0;
    background:
      radial-gradient(ellipse 200px 260px at 86% 45%, rgba(255,255,255,.85), rgba(243,182,226,.6) 45%, transparent 75%),
      radial-gradient(ellipse 320px 200px at 30% 40%, rgba(255,255,255,.35), transparent 70%);
  }
  .card-shapes { position: absolute; inset: 0; }
  .brand {
    position: absolute;
    left: 58px;
    top: 56px;
    font-size: 40px;
    font-weight: 600;
    color: var(--magenta);
    line-height: 1.2;
  }
  .tagline {
    position: absolute;
    left: 60px;
    top: 112px;
    font-size: 16px;
    font-weight: 400;
    color: var(--white);
    letter-spacing: 0.5px;
  }
  .contact {
    position: absolute;
    left: 335px;
    top: 178px;
    color: var(--white);
  }
  .contact-name {
    font-size: 20px;
    color: var(--magenta-bright);
    margin-bottom: 6px;
  }
  .contact-list { list-style: none; padding-left: 20px; }
  .contact-list li {
    display: flex;
    align-items: center;
    gap: 10px;
    font-size: 14px;
    line-height: 24px;
    white-space: nowrap;
  }
  .contact-icon { width: 14px; height: 14px; flex: none; }
</style>
</head>
<body>

<article class="card">
  <div class="card-art" role="img" aria-label="Soft blue burst of light with radiating rays and glowing dots"></div>
  <svg class="card-shapes" viewBox="0 0 700 400" aria-hidden="true">
    <polygon points="0,230 310,400 0,400" fill="var(--magenta)"/>
    <polygon points="430,0 700,0 700,250" fill="var(--magenta)" opacity="0.9"/>
  </svg>
  <div class="brand">Marla's Elixirs</div>
  <div class="tagline">....a little bit of magic</div>
  <div class="contact">
    <p class="contact-name">Yvonne Hart-Becker</p>
    <ul class="contact-list">
      <li><svg class="contact-icon" viewBox="0 0 14 14"><path d="M2 4c0-2 10-2 10 0l-2 2-2-1H6L4 6z M3 7h8l1 5H2z" fill="var(--magenta-bright)"/></svg>800-555-7341</li>
      <li><svg class="contact-icon" viewBox="0 0 14 14"><rect x="1" y="3" width="12" height="8" fill="var(--magenta-bright)"/><path d="M1 3l6 5 6-5" stroke="#fff" fill="none"/></svg>Yvonne@MarlasElixirs-example.com</li>
      <li><svg class="contact-icon" viewBox="0 0 14 14"><circle cx="7" cy="7" r="6" fill="var(--magenta-bright)"/><path d="M1 7h12M7 1c-3 3-3 9 0 12M7 1c3 3 3 9 0 12" stroke="#fff" fill="none" stroke-width="1"/></svg>www.MarlasElixirs-example.com</li>
    </ul>
  </div>
</article>

<article class="card">
  <div class="card-art" role="img" aria-label="Soft blue burst of light with radiating rays and glowing dots"></div>
  <svg class="card-shapes" viewBox="0 0 700 400" aria-hidden="true">
    <polygon points="0,230 310,400 0,400" fill="var(--magenta)"/>
    <polygon points="430,0 700,0 700,250" fill="var(--magenta)" opacity="0.9"/>
  </svg>
  <div class="brand">Marla's Elixirs</div>
  <div class="tagline">....a little bit of magic</div>
  <div class="contact">
    <p class="contact-name">Tobias Werner</p>
    <ul class="contact-list">
      <li><svg class="contact-icon" viewBox="0 0 14 14"><path d="M2 4c0-2 10-2 10 0l-2 2-2-1H6L4 6z M3 7h8l1 5H2z" fill="var(--magenta-bright)"/></svg>800-555-7341</li>
      <li><svg class="contact-icon" viewBox="0 0 14 14"><rect x="1" y="3" width="12" height="8" fill="var(--magenta-bright)"/><path d="M1 3l6 5 6-5" stroke="#fff" fill="none"/></svg>Tobias@MarlasElixirs-example.com</li>
      <li><svg class="contact-icon" viewBox="0 0 14 14"><circle cx="7" cy="7" r="6" fill="var(--magenta-bright)"/><path d="M1 7h12M7 1c-3 3-3 9 0 12M7 1c3 3 3 9 0 12" stroke="#fff" fill="none" stroke-width="1"/></svg>www.MarlasElixirs-example.com</li>
    </ul>
  </div>
</article>

</body>
</html>
```